Photography Business, Business Card

Looking for a unique cutting edge card that takes advantage of the latest printing technologies. Please review this site for all the options they office: https://plumeprints.example. If you can think it they can do it. And if you have an idea and do not know if they can do it, I will check into it.
Updates

Target Market(s)

People and places I took images of and future clients.

Industry/Entity Type

Photography

Contact Information for Business Card

Name, cell & email. Colin Hartley, chartley@kvnphoto.example, 318-742-9061

Colors

Designer to choose only greyscale colors for use in the design.

Requirements
Must have
• 100% cutting edge. Is so great, those I hand it to always show it to someone else. A piece of art.
Nice to have
• Blacks, silvers, greys, some red. Maybe other colors?

```html
<!DOCTYPE html>
<html lang="en">
<head>
<meta charset="UTF-8">
<title>Colin Hartley — Photography Business Card</title>
<link href="https://fonts.googleapis.com/css2?family=Questrial&display=swap" rel="stylesheet">
<style>
  :root {
    --stage: #eceef0;
    --clear-top: #e9ecee;
    --clear-bottom: #cdd2d6;
    --clear-edge: #a9b0b5;
    --band: #1c1c1c;
    --band-edge: #2a2a2a;
    --text-light: #e6e6e6;
    --accent-red: #d42a2a;
    --lens-area: #1e1b1b;
  }
  * { margin: 0; padding: 0; box-sizing: border-box; }
  html, body { width: 1200px; height: 1200px; overflow: hidden; }
  body {
    background: var(--stage);
    font-family: "Questrial", "Century Gothic", sans-serif;
  }
  .canvas {
    position: relative;
    width: 1200px;
    height: 1200px;
  }
  .card {
    position: absolute;
    top: 320px;
    width: 330px;
    height: 548px;
    border-radius: 165px 165px 6px 6px;
    background: linear-gradient(180deg, var(--clear-top) 0%, var(--clear-bottom) 100%);
    border: 2px solid var(--clear-edge);
    overflow: hidden;
    box-shadow: 0 10px 30px rgba(0,0,0,0.12);
  }
  .card--front { left: 215px; }
  .card--back { left: 655px; }
  .lens-photo {
    position: absolute;
    top: 38px;
    left: 50%;
    width: 256px;
    height: 256px;
    margin-left: -128px;
    border-radius: 50%;
    background: var(--lens-area);
  }
  .info-band {
    position: absolute;
    left: 0;
    right: 0;
    bottom: 0;
    height: 122px;
    background: var(--band);
    border-top: 1px solid var(--band-edge);
    color: var(--text-light);
  }
  .info-band--identity {
    display: flex;
    flex-direction: column;
    align-items: center;
    justify-content: center;
    gap: 6px;
  }
  .brand-name {
    color: var(--accent-red);
    font-size: 44px;
    letter-spacing: 6px;
    line-height: 1;
  }
  .person-name {
    font-size: 31px;
    line-height: 1.1;
  }
  .info-band--contact {
    display: flex;
    flex-direction: column;
    justify-content: center;
    gap: 16px;
    padding-left: 22px;
  }
  .contact-line {
    display: flex;
    align-items: center;
    gap: 14px;
    font-size: 19px;
    white-space: nowrap;
  }
  .contact-line--phone { padding-left: 62px; }
  .contact-icon { width: 20px; height: 20px; fill: var(--accent-red); flex: none; }
</style>
</head>
<body>
  <main class="canvas">
    <section class="card card--front" aria-label="Card front">
      <div class="lens-photo" role="img" aria-label="Photograph of a camera lens"></div>
      <div class="info-band info-band--identity">
        <span class="brand-name">KVN</span>
        <span class="person-name">Colin Hartley</span>
      </div>
    </section>

    <section class="card card--back" aria-label="Card back">
      <div class="lens-photo" role="img" aria-label="Photograph of a camera lens"></div>
      <div class="info-band info-band--contact">
        <div class="contact-line contact-line--phone">
          <svg class="contact-icon" viewBox="0 0 24 24" aria-hidden="true">
            <path d="M6.6 10.8c1.4 2.8 3.8 5.1 6.6 6.6l2.2-2.2c.3-.3.7-.4 1-.2 1.1.4 2.3.6 3.6.6.6 0 1 .4 1 1V20c0 .6-.4 1-1 1C10.6 21 3 13.4 3 4c0-.6.4-1 1-1h3.5c.6 0 1 .4 1 1 0 1.3.2 2.5.6 3.6.1.3 0 .7-.2 1L6.6 10.8z"/>
          </svg>
          <span>318-742-9061</span>
        </div>
        <div class="contact-line">
          <svg class="contact-icon" viewBox="0 0 24 24" aria-hidden="true">
            <path d="M3 5h18c.6 0 1 .4 1 1v12c0 .6-.4 1-1 1H3c-.6 0-1-.4-1-1V6c0-.6.4-1 1-1zm9 7.2L4.5 7v1.8L12 14l7.5-5.2V7L12 12.2z"/>
          </svg>
          <span>chartley@kvnphoto.example</span>
        </div>
      </div>
    </section>
  </main>
</body>
</html>
```